domestic violence campaign

To Whom It May Concern:

We are fully aware that domestic violence can enter anyone’s life at any given time. As women we are faced with many demands as mothers, daughters, wives, sisters, providers, and friends. We often lose ourselves and our confidence. Harbor of Hope (HOH) Transitional Center of Western New York has embarked on a whole new way of intervention and prevention. As a domestic violence survivor I have created a facility and ideals which will enforce a revolution of Domestic Violence victims. For many years, growing up in suburbs of Western New York, I have come to terms with this fight. Domestic Violence can be stopped and prevented. As a domestic violence victim myself, being in live-in facility, as well as six different domestic violence shelters throughout the state, I fled from my domestic violence abuse. Without those temporary facilities, all that comes to my mind is death. They helped me rebuild and save my life but something was missing – zero education, training programs, parenting classes, personal strengthening workshops, on site at all. Considering the limited amount of time (30-45 days in an average shelter) and lack of resources, I was in need of the tools needed to move me from being a victim to having a stable life.
Opening more doors in Western New York is essential with the surrounding agencies and shelters overwhelmed from assisting women of crisis. Many issues have risen, as a result, such as: over-crowding, long waiting lists, and zero educational training with an on-site teaching curriculum. A repeated vicious cycle – victims regressing and not progressing with over 4000 cases of domestic violence reported throughout Erie County. The opening Harbor of Hope (HOH) Transitional Center of Western New York will provide a 9-24 month live-in facility, along with educational and training programs on-site that will serve as important tools to domestic violence victims. These educational based facilities and services are well needed for Western New York. Our trained certified staff will provide endless help to domestic violence victim. They will feel safe as they rebuild their lives and take advantage of our educational curriculum that has been designed to increase awareness and provide steppingstones to move the victims into confident stable independent human beings. Our clients will receive complete educational training, state testing, parenting classes, as well as strengthening, coping, and developing skills here at our facility. Harbor of Hope (HOH) Transitional Center is asking for your support.
Sincerely,
Marlena Brooks
President and CEO/website hohtcq.example
Harbor of Hope (HOH) Transitional Center of WNY

Industry/Entity Type

Training

Requirements
Nice to have
• we have already created our T-shirt/we will like for our T-shirt to be the center of the campaign to T-shirt reads
V IOLENCE
O N
W OMEN
S TOPS the campaign is to raise money so we can open doors and save lives

```html
<!DOCTYPE html>
<html lang="en">
<head>
<meta charset="utf-8">
<title>Violence On Women Stops – Harbor of Hope</title>
<link rel="stylesheet" href="https://fonts.googleapis.com/css2?family=Ubuntu:wght@500;700&family=Source+Sans+3:ital,wght@0,400;1,400;1,700&display=swap">
<style>
  :root {
    --purple: #4e1d5a;
    --purple-deep: #3a1245;
    --purple-light: #6a2f78;
    --brand: #7b2a8c;
    --white: #ffffff;
    --paper: #f4f4f5;
    --paper-shade: #d9d9dc;
    --ink: #555559;
    --ink-dark: #4a4a4e;
  }
  html, body { margin: 0; padding: 0; overflow: hidden; }
  body { width: 1200px; height: 929px; background: var(--paper); }
  .campaign {
    position: relative; width: 1200px; height: 929px; overflow: hidden;
    background: linear-gradient(180deg, var(--white) 0%, var(--paper) 40%, var(--paper-shade) 100%);
    font-family: "Source Sans 3", sans-serif;
  }
  .band { position: absolute; left: 0; top: 0; width: 1200px; height: 929px; }
  .brand {
    position: absolute; left: 130px; top: 74px;
    display: flex; align-items: center; gap: 18px;
  }
  .brand-dot { width: 64px; height: 64px; border-radius: 50%; background: var(--brand); }
  .brand-name {
    font-family: "Source Sans 3", sans-serif; font-weight: 400; color: var(--brand);
    font-size: 29px; line-height: 1.15;
  }
  .donate {
    position: absolute; left: 690px; top: 0; width: 420px; height: 250px;
    text-align: center; color: var(--white);
  }
  .donate-title {
    font-family: "Ubuntu", sans-serif; font-weight: 700; font-size: 52px;
    line-height: 50px; margin: 58px 0 0; letter-spacing: 1px;
  }
  .donate-url { font-size: 28px; line-height: 34px; margin-top: 8px; white-space: nowrap; }
  .photo { position: absolute; left: 0; top: 0; }
  .message {
    position: absolute; left: 500px; top: 318px; width: 680px;
    text-align: center; color: var(--white);
  }
  .message .head {
    font-family: "Ubuntu", sans-serif; font-weight: 700; font-size: 47px;
    letter-spacing: 2px; line-height: 56px; margin: 0;
  }
  .message .line { font-size: 32px; line-height: 44px; margin: 8px 0 0; }
  .message .head.time { margin-top: 6px; }
  .vows-card {
    position: absolute; left: 160px; top: 575px; width: 290px; height: 440px;
    background: linear-gradient(160deg, var(--purple-light), var(--purple-deep));
    border: 7px solid var(--white); border-radius: 34px;
    transform: rotate(-13deg); box-shadow: 0 4px 14px rgba(0,0,0,.35);
    color: var(--white); font-family: "Ubuntu", sans-serif;
  }
  .vows-line { position: absolute; white-space: nowrap; font-weight: 500; font-size: 27px; letter-spacing: 5px; }
  .vows-line b { font-weight: 700; font-size: 52px; letter-spacing: 0; margin-right: 10px; }
  .vows-line.v { left: 30px; top: 40px; }
  .vows-line.o { left: 44px; top: 112px; }
  .vows-line.w { left: 58px; top: 184px; }
  .vows-line.s { left: 72px; top: 256px; }
  .pledge {
    position: absolute; left: 520px; top: 688px; width: 600px;
    text-align: center; color: var(--ink); font-style: italic;
  }
  .pledge p { margin: 0; }
  .pledge .lead { font-size: 32px; line-height: 40px; }
  .pledge .vow-title { font-weight: 700; font-size: 41px; color: var(--ink-dark); line-height: 48px; }
  .pledge .call { font-size: 31px; margin-top: 12px; line-height: 40px; }
  .pledge .phone { font-weight: 700; font-size: 45px; color: var(--ink-dark); line-height: 54px; }
</style>
</head>
<body>
<main class="campaign">
  <svg class="band" viewBox="0 0 1200 929" aria-hidden="true">
    <defs>
      <radialGradient id="bandFill" cx="0.55" cy="0.4" r="0.7">
        <stop offset="0" stop-color="#5e2670"/>
        <stop offset="1" stop-color="#3d1449"/>
      </radialGradient>
      <radialGradient id="ovalFill" cx="0.5" cy="0.4" r="0.6">
        <stop offset="0" stop-color="#5f2770"/>
        <stop offset="1" stop-color="#3d1449"/>
      </radialGradient>
    </defs>
    <path d="M0 250 C 250 235, 430 275, 640 285 C 850 295, 1040 255, 1200 225 L1200 653 L0 653 Z" fill="url(#bandFill)"/>
    <ellipse cx="900" cy="100" rx="210" ry="150" fill="url(#ovalFill)" stroke="#ffffff" stroke-width="6"/>
  </svg>

  <svg class="photo" width="1200" height="929" role="img" aria-label="Photograph of a frightened woman shielding her head from a raised fist">
    <defs>
      <linearGradient id="photoFill" x1="0" y1="0" x2="1" y2="0">
        <stop offset="0" stop-color="#8c8c8e"/>
        <stop offset="0.55" stop-color="#d8d8d8"/>
        <stop offset="1" stop-color="#e9e9e9" stop-opacity="0"/>
      </linearGradient>
    </defs>
    <path d="M0 250 C 200 238, 380 262, 520 275 L520 653 L0 653 Z" fill="url(#photoFill)"/>
  </svg>

  <div class="brand">
    <span class="brand-dot" aria-hidden="true"></span>
    <div class="brand-name">Harbor of Hope<br>Transitional Center<br>Western New York</div>
  </div>

  <div class="donate">
    <p class="donate-title">DONATE<br>TODAY</p>
    <div class="donate-url">www.hohtcq.example</div>
  </div>

  <section class="message">
    <h1 class="head">DOMESTIC VIOLENCE</h1>
    <p class="line">can enter anyone’s life at any given</p>
    <p class="head time">TIME</p>
    <p class="line">Domestic Violence can be stopped or</p>
    <p class="head">PREVENTED</p>
  </section>

  <div class="vows-card">
    <div class="vows-line v"><b>V</b>iolence</div>
    <div class="vows-line o"><b>O</b>n</div>
    <div class="vows-line w"><b>W</b>omen</div>
    <div class="vows-line s"><b>S</b>tops</div>
  </div>

  <section class="pledge">
    <p class="lead">Place your Ad, and speak out take the</p>
    <p class="vow-title">“Vows with HOH”</p>
    <p class="call">Call Today for More Information</p>
    <p class="phone">(716) 555-0142</p>
  </section>
</main>
</body>
</html>
```